Dashboard Elements

Hello – looking for someone to create dashboard elements.
I’ve already basically designed all these elements – but I need someone to take what I’ve designed and make it look like an actual dashboard UI, like an app - assuming using some kind of dashboard UI kit (but however you would like to get it done is fine). It can look just like mine or try something different, as long as it matches the color scheme webpage that I’m going to out it on – see the page here. I’m ok with making it dark, maybe that would look better – again as long as it matches the webpage (https://www.plandeck.io/file/7KqWmb2TxRpLnVc4Hd8Fs3/Webpage-with-placeholders?node-id=0%3A1). Please note, you do not need to put anything on the webpage or do anything with this Figma file, this is just a reference so you can color/stylize it accordingly.

The attached Powerpoint file has everything you need - make sure to zoom all the way out to see everything on the slides.

Here are the Dashboard elements needed (this will all make sense when you look at the PPT):
Dashboard 1
Dashboard 1 – expanded view A
Dashboard 1 – expanded view B
View Source button by itself
Source Document Viewer 1 and 2 (these are exactly the same just with a different image inside)*
Dashboard 2 (only slightly different than Dashboard 1, just extended with extra headings
Table of Contents
Searchbar and Source Doc by itself
*the documents in the source document viewers should still look like documents - they don’t need to look like part of the UI, because this is a document viewer – you can restyle/recolor if necessary or just leave these as is.
- Colors must match color scheme of webpage, attached and on Figma link (images there currently are only placeholders) – ok to go dark as long as it matches
- Must look sleek, clean, realistic
- Don’t add any pictures of people or change the text.
- In case it’s not clear, this is what I mean by the concept of Dashboard UI - https://www.quillbin.com/shard/s7/sh/8c1d2fa0-42b7-9a3e-7d5c-03b8e1f9a6d4/71c4e2a09b3f6d58e2a1c7f04b9d3e62
- Must be sent in an editable file, I may need to be edit text and other elements
- If you are going to send a sample, please make sure it’s part of the dashboard itself, not just the table of contents etc

Ideally hoping to find someone I can continue working with as I'll have a lot more graphic design work needed coming up.

Thank you!

```html
<!DOCTYPE html>
<html lang="en">
<head>
<meta charset="utf-8">
<title>MEDPANE – C-CDA Compendium Dashboard Elements</title>
<link rel="stylesheet" href="https://fonts.googleapis.com/css2?family=Chakra+Petch:wght@500;600&family=Inter:wght@400;500;600&family=Arimo:wght@400;700&family=Courier+Prime&family=Tinos:ital@1&display=swap">
<style>
:root{
  --bg:#100f24;
  --panel-top:#1d2458;
  --panel-mid:#161a40;
  --panel-bot:#13163a;
  --row:#1a1e46;
  --row-line:rgba(255,255,255,.07);
  --band-a:#4a4192;
  --band-b:#2c3b8c;
  --teal:#23c7bf;
  --teal-dark:#1b7c85;
  --blue:#3a8dff;
  --text:#f2f3fb;
  --muted:#b9bcdc;
  --card:#262b4e;
  --paper:#ffffff;
  --ink:#1c1c1c;
  --highlight:#a8e1d4;
}
*{box-sizing:border-box;margin:0;padding:0}
html,body{width:1200px;height:1060px;overflow:hidden;background:var(--bg)}
body{font-family:"Inter",sans-serif;color:var(--text)}
.board{position:absolute;left:0;top:0;width:2044px;height:1806px;transform:scale(.58708);transform-origin:0 0}
.abs{position:absolute}
.panel{position:absolute;overflow:hidden;background:linear-gradient(180deg,var(--panel-top) 0%,var(--panel-mid) 45%,var(--panel-bot) 100%)}
.brand{position:absolute;left:23px;top:22px;display:flex;align-items:center;gap:10px;font-size:14px;letter-spacing:.5px;white-space:nowrap}
.brand-mark{width:12px;height:12px;background:var(--teal);border-radius:2px}
.brand-sep{color:var(--muted);margin:0 6px}
.caps{font-family:"Chakra Petch",sans-serif;font-weight:600;letter-spacing:1px;text-transform:uppercase}
.brand .caps{font-size:11px}
.patient{position:absolute;right:23px;top:50px;text-align:right;white-space:nowrap}
.patient-name{font-family:"Chakra Petch",sans-serif;font-weight:500;font-size:20px;letter-spacing:2px}
.patient-meta{font-size:12px;margin-top:6px;font-weight:500}
.patient-meta i{font-style:normal;color:var(--teal);margin:0 7px;font-size:9px;vertical-align:1px}
.summary{position:absolute;left:23px;right:23px;display:flex;justify-content:space-between;align-items:center;white-space:nowrap}
.summary .caps{font-size:10.5px;letter-spacing:.6px}
.summary .teal{color:var(--teal)}
.summary .pipe{margin:0 9px}
.chev{display:inline-block;width:7px;height:7px;border-right:1.5px solid currentColor;border-bottom:1.5px solid currentColor;transform:rotate(45deg) translate(-2px,-2px)}
.chev.up{transform:rotate(-135deg) translate(-1px,-1px);margin-left:10px}
.grid-row{display:grid;grid-template-columns:90px 282px 91px 36px 1fr;align-items:center;padding:0 23px;white-space:nowrap}
.thead{height:45px;background:linear-gradient(90deg,var(--band-a),var(--band-b));font-size:10px;color:#c9cbee}
.thead.caps{letter-spacing:.6px}
.thead>span{display:flex;align-items:center;gap:6px}
.thead.multi>span{align-items:flex-start;line-height:17px}
.thead.multi .sort{margin-top:4px}
.sort{width:6px;height:9px;flex:none}
.trow{height:45px;background:var(--row);border-bottom:1px solid var(--row-line);font-size:12px;font-weight:500}
.trow .code{color:var(--teal);font-weight:600}
.trow .raf{color:var(--teal);font-weight:600}
.trow .end{justify-self:end;color:var(--teal)}
.cols6{grid-template-columns:89px 133px 83px 70px 86px 1fr}
.section-title{position:absolute;left:23px;font-size:12px}
.why{font-size:11px;font-weight:500;white-space:nowrap}
.why b{color:var(--blue);font-weight:600}
.label{font-size:11px;font-weight:500;line-height:14px;white-space:nowrap}
.link{font-family:"Chakra Petch",sans-serif;font-weight:600;font-size:11px;color:var(--blue);letter-spacing:.3px;white-space:nowrap}
.btn-source{position:absolute;display:flex;align-items:center;justify-content:center;gap:8px;width:105px;height:27px;background:var(--teal-dark);color:#dffcff;border-radius:2px;font-family:"Chakra Petch",sans-serif;font-weight:600;font-size:10px;letter-spacing:1px;white-space:nowrap}
.btn-source svg{width:9px;height:11px}
.float-card{position:absolute;background:var(--card);border-radius:4px;box-shadow:0 10px 30px rgba(0,0,0,.35)}
.doc-panel .doc-title{position:absolute;left:23px;top:118px;font-size:13px;white-space:nowrap}
.doc-tools{position:absolute;right:23px;top:117px;display:flex;gap:22px;color:var(--teal)}
.doc-tools svg{width:18px;height:18px}
.paper{position:absolute;left:24px;top:155px;width:509px;height:447px;background:var(--paper);border-radius:4px;overflow:hidden;color:var(--ink);font-family:"Arimo",sans-serif}
.scroll{position:absolute;right:17px;top:27px;width:4px;height:68px;border-radius:2px;background:var(--blue)}
.scroll-track{position:absolute;right:17px;top:27px;width:4px;height:400px;border-radius:2px;background:#eef0f4}
.paper .t{position:absolute;white-space:nowrap}
.mono{font-family:"Courier Prime",monospace}
.toc-item{height:26px;display:flex;align-items:center;padding-left:15px;font-size:10px;font-weight:500;background:#1e2350;border-bottom:1px solid rgba(255,255,255,.05)}
.toc-item.active{background:var(--teal)}
.search{position:absolute;height:25px;background:#eef0f8;border-radius:3px;display:flex;align-items:center;padding-left:15px;font-family:"Chakra Petch",sans-serif;font-weight:600;font-size:9px;letter-spacing:1px;color:#a7abc4;white-space:nowrap}
.lab-row{position:absolute;left:0;right:0;height:45px;display:flex;align-items:center;border-bottom:1px solid var(--row-line);font-size:10px;font-weight:500;white-space:nowrap}
.lab-row>*{position:absolute}
.lab-row .val{font-size:12px}
.status{color:var(--teal);font-weight:600;display:flex;align-items:center;gap:9px;font-size:10.5px}
.status.low{font-size:12px}
.status svg{width:9px;height:11px}
.p02{color:var(--blue);font-size:11px}
</style>
</head>
<body>
<svg width="0" height="0" style="position:absolute">
  <symbol id="i-sort" viewBox="0 0 6 9"><path d="M3 0 6 3.5H0zM3 9 0 5.5h6z" fill="currentColor"/></symbol>
  <symbol id="i-doc" viewBox="0 0 9 11"><path d="M.5.5h5l3 3v7h-8z" fill="none" stroke="currentColor"/><path d="M2.5 6h4M2.5 8h4" stroke="currentColor"/></symbol>
  <symbol id="i-down" viewBox="0 0 18 18"><path d="M9 2v10M4.5 8 9 12.5 13.5 8M2 16h14" fill="none" stroke="currentColor" stroke-width="1.8"/></symbol>
  <symbol id="i-print" viewBox="0 0 18 18"><path d="M4.5 6V2h9v4M4.5 13H2V6h14v7h-2.5M4.5 10h9v6h-9z" fill="none" stroke="currentColor" stroke-width="1.6" stroke-linejoin="round"/></symbol>
  <symbol id="i-up" viewBox="0 0 9 11"><path d="M4.5 0 9 4.5H6V11H3V4.5H0z" fill="currentColor"/></symbol>
  <symbol id="i-dn" viewBox="0 0 9 11"><path d="M4.5 11 0 6.5h3V0h3v6.5h3z" fill="currentColor"/></symbol>
  <symbol id="i-search" viewBox="0 0 12 12"><circle cx="5" cy="5" r="3.8" fill="none" stroke="currentColor" stroke-width="1.4"/><path d="M8 8l3 3" stroke="currentColor" stroke-width="1.4"/></symbol>
</svg>

<main class="board">

  <!-- Dashboard 1 -->
  <section class="panel" style="left:98px;top:117px;width:556px;height:443px">
    <div class="brand"><span class="brand-mark"></span>MEDPANE<span class="brand-sep">›</span><span class="caps">C-CDA Compendium</span></div>
    <div class="patient"><div class="patient-name">PATIENT MARY</div><div class="patient-meta">Female<i>●</i>01/11/1951<i>●</i>Age 70</div></div>
    <div class="summary" style="top:115px"><span class="caps">HCC Summary ( 7 )<span class="chev up"></span></span><span class="caps"><span class="teal">RAF: 2.362</span><span class="pipe">|</span>Condition Count: 8<span class="pipe">|</span>ID: 7326472</span></div>
    <div class="abs" style="left:0;right:0;top:146px">
      <div class="grid-row thead caps"><span>ICD-10 Code<svg class="sort"><use href="#i-sort"/></svg></span><span>Condition<svg class="sort"><use href="#i-sort"/></svg></span><span>Category<svg class="sort"><use href="#i-sort"/></svg></span><span>RAF<svg class="sort"><use href="#i-sort"/></svg></span><span></span></div>
      <div class="grid-row trow"><span class="code">J44.9</span><span>Chronic Obstructive Pulmonary Disease</span><span>111</span><span class="raf">0.335</span><span class="end"><span class="chev"></span></span></div>
      <div class="grid-row trow"><span class="code">F33.1</span><span>Chronic Kidney Disease, Moderate ( Stage 3 )</span><span>138</span><span class="raf">0.069</span><span class="end"><span class="chev"></span></span></div>
      <div class="grid-row trow"><span class="code">F33.0</span><span>Major Depressive Disorder, Recurrent, Mild</span><span>59</span><span class="raf">0.309</span><span class="end"><span class="chev"></span></span></div>
      <div class="grid-row trow"><span class="code">FI42.9</span><span>Cardiomyopathy</span><span>85</span><span class="raf">0.447</span><span class="end"><span class="chev"></span></span></div>
      <div class="grid-row trow"><span class="code">E11.36</span><span>Type 2 DiabetesMellitus with Diabetic Cataract</span><span>18</span><span class="raf">0.302</span><span class="end"><span class="chev"></span></span></div>
      <div class="grid-row trow"><span class="code">J44.9</span><span>Chronic Obstructive Pulmonary Disease</span><span>111</span><span class="raf">0.335</span><span class="end"><span class="chev"></span></span></div>
    </div>
  </section>

  <!-- Dashboard 1 – expanded view A -->
  <section class="panel" style="left:744px;top:117px;width:556px;height:443px;background:#141737">
    <div class="grid-row trow abs" style="left:0;right:0;top:-22px"><span class="code">FI42.9</span><span>Cardiomyopathy</span><span>85</span><span class="raf">0.447</span><span class="end"><span class="chev"></span></span></div>
    <div class="grid-row trow abs" style="left:0;right:0;top:23px;background:#1e2350"><span class="code">E11.36</span><span>Type 2 DiabetesMellitus with Diabetic Cataract</span><span>18</span><span class="raf">0.302</span><span class="end"><span class="chev"></span></span></div>
    <p class="why abs" style="left:35px;top:89px"><b>Why:</b> This patient was treated for cataracts that may be associated with type 2 diabetes mellitus.</p>
    <p class="label abs" style="left:35px;top:122px">Extracapsular Cataract<br>with IOL</p>
    <span class="link abs" style="left:176px;top:122px">C-CDA: Procedures</span>
    <span class="btn-source" style="left:416px;top:122px"><svg><use href="#i-doc"/></svg>VIEW SOURCE</span>
    <p class="label abs" style="left:35px;top:278px">Diabetes Type 2</p>
    <span class="link abs" style="left:176px;top:278px">C-CDA: Problem List</span>
    <span class="btn-source" style="left:416px;top:277px"><svg><use href="#i-doc"/></svg>VIEW SOURCE</span>
    <div class="grid-row trow abs" style="left:0;right:0;top:418px;background:#1e2350"><span class="code">J44.9</span><span>Chronic Obstructive Pulmonary Disease</span><span>111</span><span class="raf">0.335</span><span class="end"><span class="chev"></span></span></div>
  </section>
  <div class="float-card" style="left:714px;top:291px;width:558px;height:78px">
    <p class="label abs" style="left:35px;top:15px">Cataract</p>
    <span class="link abs" style="left:176px;top:16px">Ophthalmology Chart Note</span>
    <p class="label abs" style="left:176px;top:34px">Patient presents for cataract evaluation<br>in the right eye.</p>
    <span class="btn-source" style="left:417px;top:14px"><svg><use href="#i-doc"/></svg>VIEW SOURCE</span>
  </div>
  <div class="float-card" style="left:773px;top:447px;width:557px;height:58px">
    <p class="label abs" style="left:35px;top:12px">HbA1c</p>
    <span class="link abs" style="left:175px;top:12px">Lab Results</span>
    <p class="label abs" style="left:175px;top:30px">Hemoglobin A1C,&nbsp; 6.9%,&nbsp; 01/15/21</p>
    <span class="btn-source" style="left:417px;top:12px"><svg><use href="#i-doc"/></svg>VIEW SOURCE</span>
  </div>

  <!-- Dashboard 1 – expanded view B -->
  <section class="panel" style="left:1390px;top:117px;width:556px;height:243px;background:#141737">
    <div class="grid-row trow abs" style="left:0;right:0;top:0;height:46px;background:#1e2350"><span class="code">F33.1</span><span>Chronic Kidney Disease, Moderate ( Stage 3 )</span><span>138</span><span class="raf">0.069</span><span class="end"><span class="chev"></span></span></div>
    <p class="why abs" style="left:35px;top:66px"><b>Why:</b> This patient has an eGFR between 45-59 mL/min.</p>
    <p class="label abs" style="left:35px;top:100px">eGFR</p>
    <span class="link abs" style="left:176px;top:100px">Lab Results</span>
    <p class="label abs" style="left:176px;top:118px">47 mL/min,&nbsp;&nbsp; 05/26/2021</p>
    <span class="link abs" style="left:176px;top:143px">History</span>
    <p class="label abs" style="left:176px;top:161px">45 mL/min,&nbsp;&nbsp; 03/17/21<br>41 mL/min,&nbsp;&nbsp; 01/14/21<br>52 mL/min,&nbsp;&nbsp; 10/15/20<br>44 mL/min,&nbsp;&nbsp; 06/22/20</p>
    <span class="btn-source" style="left:425px;top:100px"><svg><use href="#i-doc"/></svg>VIEW SOURCE</span>
  </section>

  <!-- View Source button -->
  <span class="btn-source" style="left:1391px;top:442px"><svg><use href="#i-doc"/></svg>VIEW SOURCE</span>

  <!-- Dashboard 2 -->
  <section class="panel" style="left:98px;top:677px;width:556px;height:901px">
    <div class="brand"><span class="brand-mark"></span>MEDPANE<span class="brand-sep">›</span><span class="caps">C-CDA Compendium</span></div>
    <div class="patient"><div class="patient-name">PATIENT MARY</div><div class="patient-meta">Female<i>●</i>01/11/1951<i>●</i>Age 70</div></div>
    <div class="summary" style="top:115px"><span class="caps">HCC Summary ( 10 )<span class="chev up"></span></span><span class="caps"><span class="teal">RAF: 2.362</span><span class="pipe">|</span>Condition Count: 8<span class="pipe">|</span>ID: 7326472</span></div>
    <h3 class="section-title caps" style="top:160px">Newly identified ICD-10 codes</h3>
    <div class="abs" style="left:0;right:0;top:189px">
      <div class="grid-row thead caps"><span>ICD-10 Code<svg class="sort"><use href="#i-sort"/></svg></span><span>Condition<svg class="sort"><use href="#i-sort"/></svg></span><span>Category<svg class="sort"><use href="#i-sort"/></svg></span><span>RAF<svg class="sort"><use href="#i-sort"/></svg></span><span></span></div>
      <div class="grid-row trow"><span class="code">I70.0</span><span>Aortic Atherosclerosis</span><span>108</span><span class="raf">0.298</span><span class="end"><span class="chev"></span></span></div>
      <div class="grid-row trow"><span class="code">F33.1</span><span>Major Depressive Disorder, Recurrent, Moderate</span><span>58</span><span class="raf">0.309</span><span class="end"><span class="chev"></span></span></div>
      <div class="grid-row trow"><span class="code">I48.2</span><span>Chronic Atrial Fibrillation</span><span>96</span><span class="raf">0.268</span><span class="end"><span class="chev"></span></span></div>
      <div class="grid-row trow"><span class="code">I20.9</span><span>Angina Pectoris</span><span>88</span><span class="raf">0.140</span><span class="end"><span class="chev"></span></span></div>
    </div>
    <h3 class="section-title caps" style="top:445px">Previously known ICD-10 codes</h3>
    <div class="abs" style="left:0;right:0;top:475px">
      <div class="grid-row thead caps"><span>ICD-10 Code<svg class="sort"><use href="#i-sort"/></svg></span><span>Condition<svg class="sort"><use href="#i-sort"/></svg></span><span>Category<svg class="sort"><use href="#i-sort"/></svg></span><span>RAF<svg class="sort"><use href="#i-sort"/></svg></span><span></span></div>
      <div class="grid-row trow" style="height:62px;line-height:17px"><span class="code">F32.9</span><span>Major Depressive Disorder, Single Episode,<br>Unspecified</span><span>N/A</span><span class="raf">0</span><span class="end"><span class="chev"></span></span></div>
      <div class="grid-row trow"><span class="code">Z79.01</span><span>Long-Term Use of Anticoagulants</span><span>N/A</span><span class="raf">0</span><span class="end"><span class="chev"></span></span></div>
      <div class="grid-row trow"><span class="code">I25.9</span><span>Chronic Ischemic Heart Disease, Unspecified</span><span>N/A</span><span class="raf">0</span><span class="end"><span class="chev"></span></span></div>
      <div class="grid-row trow"><span class="code">D45</span><span>Polycythemia Vera</span><span>48</span><span class="raf">0.312</span><span class="end"><span class="chev"></span></span></div>
      <div class="grid-row thead caps multi cols6" style="height:62px"><span><span>ICD-10<br>Category</span><svg class="sort"><use href="#i-sort"/></svg></span><span><span>Condition</span><svg class="sort"><use href="#i-sort"/></svg></span><span><span>Predicted<br>%</span><svg class="sort"><use href="#i-sort"/></svg></span><span><span>Cohort<br>%</span><svg class="sort"><use href="#i-sort"/></svg></span><span><span>Difference</span><svg class="sort"><use href="#i-sort"/></svg></span><span><span>Change<br>%</span><svg class="sort"><use href="#i-sort"/></svg></span></div>
      <div class="grid-row trow cols6" style="height:62px;line-height:17px"><span class="code">F32.9</span><span>Hypertensive Heart<br>Disease</span><span>72.7%</span><span>22.5%</span><span>50.2</span><span>3.23%</span></div>
      <div class="grid-row trow cols6" style="height:62px;line-height:17px"><span class="code">I20.9</span><span>Type 2 Diabetes<br>Mellitus</span><span>56.8%</span><span>53.4</span><span>3.4</span><span>1.06%</span></div>
    </div>
  </section>

  <!-- Source Document Viewer 1 -->
  <section class="panel doc-panel" style="left:681px;top:630px;width:556px;height:610px">
    <div class="brand"><span class="brand-mark"></span>MEDPANE<span class="brand-sep">›</span><span class="caps">C-CDA Compendium</span></div>
    <div class="patient"><div class="patient-name">PATIENT MARY</div><div class="patient-meta">Female<i>●</i>01/11/1951<i>●</i>Age 70</div></div>
    <h2 class="doc-title caps">Document Name ( 1 )<span class="chev up"></span></h2>
    <div class="doc-tools"><svg><use href="#i-down"/></svg><svg><use href="#i-print"/></svg></div>
    <article class="paper">
      <div class="scroll-track"></div><div class="scroll"></div>
      <span class="abs" style="left:62px;top:40px;width:14px;height:14px;border-radius:50%;background:#8a8a8a"></span>
      <span class="t" style="left:60px;top:68px;font-size:10px;color:#333">Hudson Eye Clinic</span>
      <span class="t" style="left:60px;top:90px;font-size:7px;color:#888">Hudson Eye Clinic ● 418 Alder Street, Suite 12 Riverton, NY 10990 ● Phone: (555) 014-2290 ● Fax: (555) 014-2291</span>
      <div class="t" style="left:60px;top:118px;font-size:11px;line-height:13px">PATIENT:<br>DATE OF BIRTH:<br>DATE:<br>DOCUMENT TYPE:<br>VISIT TYPE:</div>
      <div class="t" style="left:174px;top:118px;font-size:11px;line-height:13px">Mary Patient<br>01/11/1951<br>04/02/2021 4:00 PM<br>Ophthalmology Chart Note<br>Office Visit</div>
      <span class="t" style="left:60px;top:197px;font-size:11px">Referring Doctor:</span>
      <span class="t" style="left:174px;top:197px;font-size:11px">Daniel Harlow</span>
      <span class="t" style="left:60px;top:228px;font-size:10px;color:#888">General</span>
      <span class="t" style="left:60px;top:242px;font-size:10px">Patient Visit: Established Patient</span>
      <div class="abs" style="left:49px;top:275px;width:404px;height:52px;background:var(--highlight)"></div>
      <span class="t" style="left:60px;top:268px;font-size:9px;color:#888">History of Present Illness</span>
      <p class="abs" style="left:60px;top:283px;width:388px;font-size:8.8px;line-height:12px;color:#3d6a63">Patient presents for cataract evaluation in the right eye. Vision is described as glare and halos, especially associated with oncoming lights while driving. In addition, patient complains of difficulty reading small print. Patient was treated 2 years ago for cataract in the left eye.</p>
      <span class="t" style="left:60px;top:331px;font-size:9.5px;color:#888">Past Ocular History</span>
      <div class="t" style="left:60px;top:345px;font-size:9.5px;line-height:12px"><b>Disease</b><br>Cataract</div>
      <div class="t" style="left:122px;top:345px;font-size:9.5px;line-height:12px"><b>Eye</b><br>OS</div>
      <div class="t" style="left:166px;top:345px;font-size:9.5px;line-height:12px"><b>Date Dx</b><br>04/15/2019</div>
      <div class="t" style="left:230px;top:345px;font-size:9.5px;line-height:12px"><b>Procedure</b><br>Phaco-PCIOL</div>
      <div class="t" style="left:307px;top:345px;font-size:9.5px;line-height:12px"><b>Date Px</b><br>06/23/2019</div>
      <div class="t" style="left:368px;top:345px;font-size:9.5px;line-height:12px"><b>Surgeon</b><br>Gene Marlow MD.</div>
      <span class="t" style="left:60px;top:388px;font-size:9.5px;color:#888">Review of Systems</span>
      <div class="t" style="left:60px;top:402px;font-size:9.5px;line-height:12px"><b>System</b><br>Constitutional<br>Eyes</div>
      <div class="t" style="left:146px;top:402px;font-size:9.5px;line-height:12px"><b>Neg/Pos</b><br>Negative<br>Negative</div>
      <div class="t" style="left:217px;top:402px;font-size:9.5px;line-height:12px"><b>Details</b><br>Fatigue and Fever<br>Diplopia, Eye Pain, Floaters and Photophobia</div>
    </article>
  </section>

  <!-- Source Document Viewer 2 -->
  <section class="panel doc-panel" style="left:1284px;top:630px;width:556px;height:610px">
    <div class="brand"><span class="brand-mark"></span>MEDPANE<span class="brand-sep">›</span><span class="caps">C-CDA Compendium</span></div>
    <div class="patient"><div class="patient-name">PATIENT MARY</div><div class="patient-meta">Female<i>●</i>01/11/1951<i>●</i>Age 70</div></div>
    <h2 class="doc-title caps">Document Name ( 1 )<span class="chev up"></span></h2>
    <div class="doc-tools"><svg><use href="#i-down"/></svg><svg><use href="#i-print"/></svg></div>
    <article class="paper" style="font-size:8.5px">
      <div class="scroll-track"></div><div class="scroll"></div>
      <span class="t" style="right:28px;top:43px;font-size:6.5px;font-family:'Tinos',serif">Mary Patient Meridian Health Network Result 02/18/2021</span>
      <span class="t" style="left:35px;top:62px;font-size:9px">PATIENT INFORMATION:</span>
      <span class="t" style="left:35px;top:72px;font-size:16px;font-weight:700">Mary Patient</span>
      <div class="t" style="left:35px;top:91px;line-height:9.5px"><b>DOB:</b>&nbsp;&nbsp;&nbsp;&nbsp;&nbsp;&nbsp;&nbsp;&nbsp; 01/11/1951<br><b>Gender:</b>&nbsp;&nbsp;&nbsp; Female</div>
      <div class="abs" style="left:181px;top:69px;width:159px;height:18px;border:1px solid #333;text-align:center;line-height:16px;font-size:8.5px">STATUS: <b>Final</b></div>
      <div class="t" style="left:173px;top:94px;line-height:9.5px"><b>Source:</b><br><b>Time Reported:</b><br><b>Received:</b></div>
      <div class="t" style="left:238px;top:94px;line-height:9.5px">Meridian Health Network<br>01/15/2021 08:35 AM<br>02/18/2021 02:23 PM</div>
      <div class="abs" style="left:35px;top:130px;width:446px;border-top:2px solid #222"></div>
      <div class="t" style="left:35px;top:132px;font-weight:700">Test</div>
      <div class="t" style="left:222px;top:132px;font-weight:700">In Range</div>
      <div class="t" style="left:297px;top:132px;font-weight:700">Out Of Range</div>
      <div class="t" style="left:380px;top:132px;font-weight:700">Reference Range</div>
      <div class="t" style="left:464px;top:132px;font-weight:700">Lab</div>
      <div class="abs" style="left:35px;top:142px;width:446px;border-top:1px solid #222"></div>
      <div class="t" style="left:38px;top:144px;line-height:9.7px">Monocytes Absolute<br>Eosinophils Absolute<br>Basophils Absolute<br>Immature Grans % (LabWorks)<br>Immature Grans Absolute (LabWorks)</div>
      <div class="t" style="left:250px;top:144px;line-height:9.7px;text-align:right">0.9<br>0.4<br>0<br>1<br>0.1</div>
      <div class="t" style="left:380px;top:144px;line-height:9.7px">0.1 - 0.9 x10E3/uL<br>x10E3/uL<br>x10E3/uL<br>Not Estab. %<br>x10E3/uL</div>
      <div class="t" style="left:467px;top:144px;line-height:9.7px;font-size:5px">P02<br>P02<br>P02<br>P02<br>P02</div>
      <div class="abs" style="left:35px;top:196px;width:446px;border-top:1px solid #222"></div>
      <div class="t" style="left:38px;top:197px;font-size:8px"><b>HEMOGLOBIN A1C, B</b>&nbsp;&nbsp;&nbsp; Collected: 01/15/2021 08:24 AM&nbsp;&nbsp;&nbsp; Reported: 01/15/2021 08:24AM</div>
      <div class="abs" style="left:28px;top:206px;width:350px;height:21px;background:var(--highlight)"></div>
      <div class="t" style="left:41px;top:208px;font-weight:700">Hemoglobin A1c</div>
      <div class="t" style="left:345px;top:208px">6.9&nbsp;&nbsp; H</div>
      <div class="t" style="left:381px;top:208px">4.8 - 5.6 %</div>
      <div class="t" style="left:467px;top:209px;font-size:5px">P02</div>
      <div class="t mono" style="left:105px;top:217px;line-height:9px;font-size:8px"><span style="color:#2f6b60">Prediabetes: 5.7 - 6.4</span><br>&nbsp;Diabetes: &gt;6.4<br>&nbsp;Glycemic control for adults with diabetes: &lt;7.0</div>
      <div class="t" style="left:38px;top:253px">Lab Interpretation</div>
      <div class="t" style="left:223px;top:253px">Abnormal</div>
      <div class="abs" style="left:35px;top:265px;width:446px;border-top:1px solid #222"></div>
      <div class="t" style="left:35px;top:267px"><b>Microalbumin/Creatinine Ratio, Urine</b>&nbsp;&nbsp;&nbsp; Collected: 08/19/2020 08:40 AM</div>
      <div class="abs" style="left:35px;top:277px;width:446px;border-top:1px solid #222"></div>
      <div class="t" style="left:38px;top:279px;line-height:9.5px">Creatinine,Ur<br>Microalbum.,U,Random<br><b>Microalb/Crt. Ratio</b></div>
      <div class="t" style="left:238px;top:279px;line-height:9.5px;text-align:right">110.2<br>71</div>
      <div class="t" style="left:341px;top:298px;font-weight:700">64&nbsp;&nbsp; H</div>
      <div class="t" style="left:380px;top:279px;line-height:9.5px">Not Estab. mg/dL<br>Not Estab. ug/mL<br>mg/g creat</div>
      <div class="t" style="left:467px;top:280px;line-height:9.5px;font-size:5px">P02<br>P02<br>P02</div>
      <div class="t mono" style="left:130px;top:309px;line-height:9px;font-size:8px">Normal:&nbsp;&nbsp;&nbsp;&nbsp;&nbsp;&nbsp;&nbsp;&nbsp;&nbsp;&nbsp;&nbsp;&nbsp;&nbsp;&nbsp;&nbsp;&nbsp;&nbsp; 0 -&nbsp; 29<br>Moderately increased: 30 - 300<br>Severely increased:&nbsp;&nbsp;&nbsp;&nbsp;&nbsp;&nbsp; &gt;300<br>&nbsp;&nbsp;&nbsp;&nbsp;**Please note reference interval change**</div>
      <div class="t mono" style="left:66px;top:345px;line-height:9px;font-size:8px">Performed At: 01<br>LabWorks Fairview<br>1280 Birch Road<br>Fairview, OH&nbsp; 44099<br>Rossi Victor PhD<br>5550142277</div>
      <div class="t" style="left:38px;top:407px">Lab Interpretation</div>
      <div class="t" style="left:223px;top:407px">Abnormal</div>
      <div class="abs" style="left:35px;top:430px;width:447px;height:14px;border:1px solid #555;padding-left:6px;line-height:12px;white-space:nowrap">P02&nbsp;&nbsp;&nbsp;&nbsp;&nbsp;&nbsp; LABWORKS 1.</div>
    </article>
  </section>

  <!-- Table of Contents -->
  <nav class="panel" style="left:771px;top:1333px;width:272px;height:362px">
    <div class="search" style="left:35px;top:24px;width:201px">TABLE OF CONTENTS&nbsp;&nbsp;<span class="chev" style="width:5px;height:5px;border-width:1.2px"></span></div>
    <div class="abs" style="left:35px;top:53px;width:201px">
      <div class="toc-item">Insurance Providers</div>
      <div class="toc-item active">Problems</div>
      <div class="toc-item">Results</div>
      <div class="toc-item">Procedures</div>
      <div class="toc-item">Encounters</div>
      <div class="toc-item">Medications</div>
      <div class="toc-item">Vital Signs</div>
      <div class="toc-item">Immunizations</div>
      <div class="toc-item">Social History</div>
      <div class="toc-item">Family History</div>
      <div class="toc-item">Plan of Care</div>
    </div>
  </nav>

  <!-- Search bar and source panel -->
  <section class="panel" style="left:1111px;top:1333px;width:557px;height:357px">
    <div class="search" style="left:334px;top:24px;width:200px;border-radius:3px 0 0 3px">RENAL FUNCTION</div>
    <div class="abs" style="left:497px;top:24px;width:37px;height:25px;background:var(--teal);border-radius:0 3px 3px 0;display:flex;align-items:center;justify-content:center;color:#fff"><svg width="11" height="11"><use href="#i-search"/></svg></div>
    <div class="abs" style="left:0;right:0;top:67px;height:63px;background:linear-gradient(90deg,var(--band-a),var(--band-b));padding:15px 23px;white-space:nowrap">
      <h2 class="caps" style="font-size:11px;letter-spacing:.4px">Renal Function Panel ( Na, K, Cl, CO2, Glu, BUN, Creat, Ca, Alk, Phos )</h2>
      <p style="font-size:10px;font-weight:600;margin-top:7px">Collected: 05/25/2021 11:38 AM&nbsp;&nbsp;&nbsp;&nbsp;&nbsp;&nbsp; Reported: 05/25/2021 11:38 AM</p>
    </div>
    <div class="lab-row" style="top:131px"><span style="left:23px">Glucose, RANDOM ( 70 - 99 mg/dL)</span><span class="val" style="left:266px">134</span><svg style="left:314px" width="45" height="14"><polyline points="0,12 12,5 20,8 32,2 45,6" fill="none" stroke="var(--teal)" stroke-width="1.2"/></svg><span class="status" style="left:374px"><svg><use href="#i-up"/></svg>Above High Normal</span><span class="p02" style="left:515px">P02</span></div>
    <div class="lab-row" style="top:176px"><span style="left:23px">BLD Urea Nitrogen ( 8 - 26 mg/dL)</span><span class="val" style="left:266px">70</span><svg style="left:314px" width="45" height="14"><polyline points="0,12 12,5 22,9 33,3 45,6" fill="none" stroke="var(--teal)" stroke-width="1.2"/></svg><span class="status" style="left:374px"><svg><use href="#i-up"/></svg>Above High Normal</span><span class="p02" style="left:515px">P02</span></div>
    <div class="lab-row" style="top:221px"><span style="left:23px">Creatinine ( 0.6 - 1.2 mg/dL )</span><span class="val" style="left:266px">1.48</span><svg style="left:314px" width="45" height="14"><polyline points="0,12 12,6 21,9 32,3 45,5" fill="none" stroke="var(--teal)" stroke-width="1.2"/></svg><span class="status" style="left:374px"><svg><use href="#i-up"/></svg>Above High Normal</span><span class="p02" style="left:515px">P02</span></div>
    <div class="lab-row" style="top:266px"><span style="left:23px">GFR Non-African Amer ( &gt;59 mL/min/1.73 m² )</span><span class="val" style="left:266px">47</span><svg style="left:314px" width="45" height="14"><polyline points="0,3 12,10 22,6 33,12 45,8" fill="none" stroke="var(--teal)" stroke-width="1.2"/></svg><span class="status low" style="left:374px"><svg><use href="#i-dn"/></svg>Below Low Normal</span><span class="p02" style="left:515px">P02</span></div>
    <div class="lab-row" style="top:311px;border-bottom:0"><span style="left:23px">GFR African American ( &gt;59 mL/min/1.73 m² )</span><span class="val" style="left:266px">55</span><svg style="left:314px" width="45" height="14"><polyline points="0,3 12,10 22,6 33,12 45,8" fill="none" stroke="var(--teal)" stroke-width="1.2"/></svg><span class="status low" style="left:374px"><svg><use href="#i-dn"/></svg>Below Low Normal</span><span class="p02" style="left:515px">P02</span></div>
  </section>

</main>
</body>
</html>
```